Reefline Aquaria Tropical Fish Startup Design

I need professional business cards and social media profiles for our tropical fish shop.

Target Market(s)

Tropical fish enthusiasts

Industry/Entity Type

Tropical Fish

Font styles to use
Sans Serif
Script
Other font styles liked:
• Comforta

Colors
0054AA
0677BA
7BADD7
CADEEF
E8F1F8
0094D4
00A9DD
6FCCEA
C7EBF8
E9F6FB
00AB8E
00BBA5
67D7C9
C6EFE9
E9F9F6

Requirements
Must have
• fish, oceanic colors
Nice to have
• Lines, boxes, anything that groups the title to stand out
Should not have
• Any punctuations

```html
<!DOCTYPE html>
<html lang="en">
<head>
<meta charset="utf-8">
<title>Reefline Aquaria Business Card</title>
<link href="https://fonts.googleapis.com/css2?family=Inter:wght@400;500;700;800&display=swap" rel="stylesheet">
<style>
  :root {
    --page: #e4e4e4;
    --ocean-deep: #003a7a;
    --ocean: #0054AA;
    --ocean-bright: #0677BA;
    --ink: #ffffff;
    --accent: #6FCCEA;
    --foam: #E9F6FB;
    --mist: #C7EBF8;
    --lagoon: #C6EFE9;
    --reef: #00BBA5;
  }
  * { margin: 0; padding: 0; box-sizing: border-box; }
  html, body { width: 1200px; height: 1200px; overflow: hidden; }
  body {
    background: var(--page);
    font-family: "Inter", sans-serif;
    position: relative;
  }
  .card {
    position: absolute;
    left: 262px;
    width: 686px;
    height: 392px;
    border-radius: 24px;
    overflow: hidden;
    background: linear-gradient(200deg, var(--ocean-bright) 0%, var(--ocean) 45%, var(--ocean-deep) 100%);
  }
  .card--front { top: 165px; }
  .card--back { top: 653px; }
  .card__edge {
    position: absolute;
    left: 0; right: 0; bottom: 0;
    height: 4px;
    background: linear-gradient(90deg, var(--reef), var(--accent));
  }

  .fish-art {
    position: absolute;
    background: linear-gradient(160deg, var(--foam) 0%, var(--mist) 60%, var(--lagoon) 100%);
  }
  .fish-art--left {
    left: 28px; top: -20px;
    width: 172px; height: 276px;
    border-radius: 30% 60% 45% 55% / 20% 35% 65% 80%;
  }
  .fish-art--right {
    left: 426px; top: 66px;
    width: 290px; height: 226px;
    border-radius: 55% 40% 30% 60% / 45% 35% 65% 55%;
  }

  .details { position: absolute; left: 202px; top: 139px; color: var(--ink); }
  .details__name {
    font-weight: 800;
    font-size: 24px;
    line-height: 26px;
    letter-spacing: -0.2px;
  }
  .details__role {
    color: var(--accent);
    font-weight: 500;
    font-size: 16px;
    line-height: 20px;
  }
  .rule {
    width: 36px;
    height: 2px;
    background: var(--ink);
    margin: 11px 0 12px;
  }
  .details__address {
    font-size: 16px;
    line-height: 19.5px;
    font-style: normal;
    letter-spacing: 0.2px;
  }
  .contact { list-style: none; }
  .contact__item {
    display: flex;
    align-items: center;
    gap: 9px;
    font-size: 16px;
    line-height: 19.5px;
    letter-spacing: 0.2px;
  }
  .contact__icon { width: 12px; height: 12px; flex: none; }

  .brand {
    position: absolute;
    left: 0; right: 0;
    top: 168px;
    text-align: center;
    color: var(--accent);
    font-weight: 700;
    font-size: 36px;
    letter-spacing: 6px;
    text-transform: uppercase;
  }
</style>
</head>
<body>
  <section class="card card--front">
    <div class="fish-art fish-art--left" role="img" aria-label="Light silhouette of a tropical fish swimming downward"></div>
    <div class="fish-art fish-art--right" role="img" aria-label="Light silhouette of a tropical cichlid swimming left"></div>

    <div class="details">
      <h1 class="details__name">DANIEL BROOKS</h1>
      <p class="details__role">President</p>
      <div class="rule"></div>
      <address class="details__address">
        Reefline Aquaria Group<br>
        4210 Harbor View Road<br>
        Coralton, Alaska 34579
      </address>
      <div class="rule"></div>
      <ul class="contact">
        <li class="contact__item">
          <svg class="contact__icon" viewBox="0 0 24 24"><path d="M6.6 10.8a15.1 15.1 0 0 0 6.6 6.6l2.2-2.2c.3-.3.7-.4 1-.2 1.1.4 2.3.6 3.6.6.6 0 1 .4 1 1V20c0 .6-.4 1-1 1A17 17 0 0 1 3 4c0-.6.4-1 1-1h3.5c.6 0 1 .4 1 1 0 1.3.2 2.5.6 3.6.1.3 0 .7-.2 1z" fill="var(--accent)"/></svg>
          555-014-2273
        </li>
        <li class="contact__item">
          <svg class="contact__icon" viewBox="0 0 24 24"><path d="M2 5h20v14H2z" fill="var(--accent)"/><path d="M2 5l10 8 10-8" fill="none" stroke="var(--ocean)" stroke-width="2"/></svg>
          info@reeflineaquaria.com
        </li>
        <li class="contact__item">
          <svg class="contact__icon" viewBox="0 0 24 24"><circle cx="12" cy="12" r="10" fill="var(--accent)"/><path d="M7 6c3 1 2 4 5 4s1 4 4 5M15 4c-1 2 1 3 3 3" fill="none" stroke="var(--ocean)" stroke-width="2"/></svg>
          reeflineaquaria.com
        </li>
      </ul>
    </div>
    <div class="card__edge"></div>
  </section>

  <section class="card card--back">
    <p class="brand">Reefline Aquaria</p>
    <div class="card__edge"></div>
  </section>
</body>
</html>
```